Small Accounting Practice needs something creative

We need a business card design for a new small accounting practice based in Perth, Australia. The name of the practice is 'Kelvarin Ledger Group Pty Ltd'. We providing Tax, Bookkeeping and Accounting services. Our target are individuals and small businesses. We want the design to be simply and creative. Also, we can the design can help us to gain people's trust.

Target Market(s)

Individuals and small businesses.

Industry/Entity Type

Accounting

Colors

Designer to choose colors to be used in the design.

```html
<!DOCTYPE html>
<html lang="en">
<head>
<meta charset="utf-8">
<title>Kelvarin Ledger Group – Business Card</title>
<link rel="stylesheet" href="https://fonts.googleapis.com/css2?family=Josefin+Slab:wght@100;200&family=Roboto:wght@400&display=swap">
<style>
  :root {
    --mint: #33ffcc;
    --paper: #ffffff;
    --ink: #3a3a3a;
    --rule: #555555;
  }
  * { margin: 0; padding: 0; box-sizing: border-box; }
  html, body {
    width: 1200px;
    height: 351px;
    overflow: hidden;
    background: var(--paper);
  }
  .card {
    position: relative;
    width: 1200px;
    height: 351px;
    background: var(--paper);
    font-family: "Roboto", Arial, sans-serif;
  }
  .card-front {
    position: absolute;
    left: 0;
    top: 0;
    width: 598px;
    height: 351px;
    background: var(--mint);
  }
  .brand-disc {
    position: absolute;
    left: 177px;
    top: 57px;
    width: 246px;
    height: 246px;
    border-radius: 50%;
    background: var(--paper);
    display: flex;
    flex-direction: column;
    align-items: center;
    justify-content: center;
  }
  .brand-name {
    color: var(--mint);
    font-family: "Roboto", Arial, sans-serif;
    font-weight: 400;
    text-align: center;
    line-height: 1;
    text-transform: uppercase;
  }
  .brand-name .brand-main {
    display: block;
    font-size: 36px;
    letter-spacing: 2px;
  }
  .brand-name .brand-sub {
    display: block;
    margin-top: 8px;
    font-size: 12.5px;
    letter-spacing: 0.2px;
  }
  .card-back {
    position: absolute;
    left: 598px;
    top: 0;
    width: 602px;
    height: 351px;
  }
  .person-name {
    position: absolute;
    right: 362px;
    top: 118px;
    text-align: right;
    font-family: "Josefin Slab", Georgia, serif;
    font-weight: 100;
    font-size: 60px;
    line-height: 56px;
    letter-spacing: 3px;
    color: var(--mint);
    text-transform: uppercase;
  }
  .divider {
    position: absolute;
    left: 248px;
    top: 117px;
    width: 1px;
    height: 116px;
    background: var(--rule);
  }
  .details {
    position: absolute;
    left: 260px;
    top: 130px;
    color: var(--ink);
    font-size: 13px;
    line-height: 1;
  }
  .details .role { display: block; }
  .details .licence { display: block; margin-top: 11px; }
  .contact {
    list-style: none;
    margin-top: 12px;
  }
  .contact li {
    display: flex;
    align-items: center;
    gap: 6px;
    height: 19px;
  }
  .contact svg { width: 10px; height: 10px; flex: none; }
</style>
</head>
<body>
  <main class="card">
    <section class="card-front">
      <div class="brand-disc">
        <p class="brand-name">
          <span class="brand-main">Kelvarin</span>
          <span class="brand-sub">Ledger Group Pty Ltd</span>
        </p>
      </div>
    </section>

    <section class="card-back">
      <h1 class="person-name">Mara<br>Quint</h1>
      <div class="divider"></div>
      <div class="details">
        <span class="role">Accountant &amp; Small Business Consultant</span>
        <span class="licence">REGISTERED ASIC AGENT 48107</span>
        <ul class="contact">
          <li>
            <svg viewBox="0 0 10 10" aria-hidden="true">
              <rect x="0" y="1" width="10" height="8" rx="2" fill="#3a3a3a"/>
              <path d="M2 3.5 L5 5.8 L8 3.5" stroke="#fff" stroke-width="1" fill="none"/>
            </svg>
            mara@kelvarinledger.com.au
          </li>
          <li>
            <svg viewBox="0 0 10 10" aria-hidden="true">
              <rect x="0" y="0" width="10" height="10" rx="2" fill="#3a3a3a"/>
              <path d="M3.3 2.2 L4.6 3.6 L4 4.4 Q4.7 5.6 5.7 6.1 L6.4 5.4 L7.8 6.7 L7 7.8 Q4.4 7.6 2.4 3.1 Z" fill="#fff"/>
            </svg>
            0491 570 226
          </li>
        </ul>
      </div>
    </section>
  </main>
</body>
</html>
```